practice letterhead

I need a letterhead design for a new company that is a veterinary specialty company. I am conservative. I want it to look professional - not "cutesy"

I need my name, credentials, address, phone number and website/email on it.

My personal information is as follows: Lorraine Aldous, DVM, DACVIM (Neurology) Certified Veterinary Pain Practitioner (or CVPP) Certified Canine Rehabilitation Therapist (or CCRT) 1487 Marden Hwy Walpole, MA 02317 508-374-6620 lorraine.aldous@kindpawspecialty.com www.kindpawspecialty.com

```html
<!DOCTYPE html>
<html lang="en">
<head>
<meta charset="utf-8">
<title>Kind Paw Veterinary Specialty Center — Letterhead</title>
<link href="https://fonts.googleapis.com/css2?family=Arimo:wght@700&family=Fjalla+One&display=swap" rel="stylesheet">
<style>
  :root {
    --canvas: #ffffff;
    --frame: #000000;
    --paper: #ffffff;
    --header-grey: #dcdcd8;
    --wave-blue: #4a70a8;
    --wave-shadow: #b7bccb;
    --brand-teal: #6a9a88;
    --brand-navy: #1f3a4a;
    --footer-bg: #333333;
    --footer-text: #ffffff;
  }
  * { margin: 0; padding: 0; box-sizing: border-box; }
  html, body {
    width: 1200px; height: 1000px; overflow: hidden;
    background: var(--canvas);
  }
  .letterhead {
    position: absolute; left: 226px; top: 16px;
    width: 750px; height: 970px;
    background: var(--paper);
    border: 3px solid var(--frame);
    border-radius: 4px;
    overflow: hidden;
  }
  .header-wave {
    position: absolute; left: 0; top: 0;
    width: 744px; height: 200px;
  }
  .brand {
    position: absolute; right: 40px; top: 40px;
    display: flex; align-items: center; gap: 14px;
  }
  .brand-dot {
    width: 58px; height: 58px; border-radius: 50%;
    background: var(--brand-navy);
  }
  .brand-name {
    font-family: "Arimo", Arial, sans-serif;
    font-weight: 700;
    color: var(--brand-teal);
    font-size: 21px;
    line-height: 1.2;
    text-align: left;
  }
  .footer {
    position: absolute; left: 0; bottom: 0;
    width: 100%; height: 49px;
    background: var(--footer-bg);
    color: var(--footer-text);
    font-family: "Fjalla One", "Arial Narrow", sans-serif;
    display: flex; justify-content: space-between;
    padding: 2px 4px 0 22px;
  }
  .footer-name { font-size: 18px; line-height: 24px; }
  .footer-credential { font-size: 12px; padding-left: 8px; line-height: 16px; }
  .footer-phone { font-size: 18px; line-height: 24px; margin-left: 40px; }
  .footer-contact { text-align: right; }
  .footer-address { font-size: 18px; line-height: 24px; padding-right: 16px; }
  .footer-web { font-size: 12px; line-height: 16px; }
</style>
</head>
<body>
  <div class="letterhead">
    <svg class="header-wave" viewBox="0 0 744 200" aria-hidden="true">
      <path d="M0,0 H744 V128 C690,158 560,172 470,164 C380,152 220,72 130,72 C60,72 15,98 0,128 Z" fill="var(--header-grey)"/>
      <path d="M0,134 C15,104 60,78 130,78 C220,78 380,158 470,170 C560,178 690,164 744,134" fill="none" stroke="var(--wave-shadow)" stroke-width="6"/>
      <path d="M0,128 C15,98 60,72 130,72 C220,72 380,152 470,164 C560,172 690,158 744,128" fill="none" stroke="var(--wave-blue)" stroke-width="5"/>
    </svg>

    <div class="brand">
      <div class="brand-dot"></div>
      <div class="brand-name">Kind Paw Veterinary<br>Specialty Center</div>
    </div>

    <footer class="footer">
      <div class="footer-person">
        <div class="footer-name">Your Name Here</div>
        <div class="footer-credential">Your Credential Here</div>
      </div>
      <div class="footer-phone">+62 012345678</div>
      <div class="footer-contact">
        <div class="footer-address">Address Here</div>
        <div class="footer-web">www.yourwebsite.com &nbsp;|&nbsp; email@yourwebsite</div>
      </div>
    </footer>
  </div>
</body>
</html>
```